Kestrelmoor business card

We're looking to "refresh" our original Kestrelmoor logo design and also get a new business card design. We're a modern consulting and software business that's been around 4-years now. We work with large professional companies and therefore require a design that is simple and professional. We would like to retain the notch in the "A" and just the word "Kestrelmoor" as the logo. We like greys, silvers, black, white...but happy to explore highlight color. We're looking for understated modern.

Industry/Entity Type

Software

```html
<!DOCTYPE html>
<html lang="en">
<head>
<meta charset="utf-8">
<title>Kestrelmoor Business Card</title>
<link rel="stylesheet" href="https://fonts.googleapis.com/css2?family=Lato:wght@400;700;900&display=swap">
<style>
  :root {
    --stage: #e4e4e4;
    --card-dark: #1c1c1c;
    --card-mid: #2c2c2c;
    --teal: #14a89a;
    --teal-light: #1fc2b2;
    --teal-deep: #0f8e82;
    --white: #ffffff;
  }
  * { box-sizing: border-box; margin: 0; padding: 0; }
  html, body {
    width: 1200px; height: 1000px; overflow: hidden;
    background: var(--stage);
    font-family: "Lato", Arial, sans-serif;
  }
  .canvas { position: relative; width: 1200px; height: 1000px; }
  .card {
    position: absolute; width: 580px; height: 330px; overflow: hidden;
    background: radial-gradient(ellipse at 55% 30%, var(--card-mid), var(--card-dark) 75%);
    box-shadow: 0 10px 26px rgba(0,0,0,0.25);
  }
  .card-front { left: 70px; top: 110px; }
  .card-back { left: 550px; top: 560px; }
  .card-shapes { position: absolute; inset: 0; width: 100%; height: 100%; }
  .wordmark {
    position: absolute; left: 0; right: 0; text-align: center;
    color: var(--white);
    font-weight: 900; font-size: 52px; letter-spacing: 1px; line-height: 1;
    text-transform: uppercase; white-space: nowrap;
  }
  .card-front .wordmark { top: 100px; }
  .web-address {
    position: absolute; left: 0; right: 0; top: 168px; text-align: center;
    color: var(--teal); font-size: 18px; letter-spacing: 5px; white-space: nowrap;
  }
  .card-back .wordmark { top: 36px; }
  .contact-block { position: absolute; left: 0; right: 0; top: 136px; text-align: center; }
  .person-name { color: var(--white); font-size: 24px; font-weight: 700; letter-spacing: 0.5px; }
  .person-title { color: var(--teal); font-size: 18px; margin-top: 4px; }
  .contact-list { list-style: none; margin-top: 30px; font-size: 16px; line-height: 1.4; color: var(--white); white-space: nowrap; }
  .contact-label { color: var(--teal); }
</style>
</head>
<body>
<main class="canvas">
  <section class="card card-front">
    <svg class="card-shapes" viewBox="0 0 580 330" preserveAspectRatio="none" aria-hidden="true">
      <polygon points="0,190 0,330 260,330" fill="var(--teal-deep)"/>
      <polygon points="0,200 290,330 0,330" fill="var(--teal)"/>
      <polygon points="0,250 260,330 0,330" fill="var(--teal-light)" opacity="0.7"/>
    </svg>
    <div class="wordmark">Kestrelmoor</div>
    <div class="web-address">www.kestrelmoor.com.au</div>
  </section>

  <section class="card card-back">
    <svg class="card-shapes" viewBox="0 0 580 330" preserveAspectRatio="none" aria-hidden="true">
      <polygon points="0,150 0,330 90,330" fill="var(--teal-deep)"/>
      <polygon points="0,190 110,330 0,330" fill="var(--teal)"/>
      <polygon points="580,250 580,330 500,330" fill="var(--teal)"/>
    </svg>
    <div class="wordmark">Kestrelmoor</div>
    <div class="contact-block">
      <div class="person-name">YOUR NAME</div>
      <div class="person-title">Title</div>
      <ul class="contact-list">
        <li><span class="contact-label">Phone:</span> 123 456 7890</li>
        <li><span class="contact-label">Mobile:</span> 123 456 7890</li>
        <li><span class="contact-label">Email:</span> yourname@kestrelmoor.com</li>
        <li><span class="contact-label">Address:</span> St. 4, Harlow Lane, Fairview, NY 10452</li>
      </ul>
    </div>
  </section>
</main>
</body>
</html>
```